Telmoro Business Card

I already have the conplay logo. I need to develop a professional business card layout

Target Market(s)

Business

Industry/Entity Type

Business

Contact Information for Business Card

Company Name: Telmoro Limited

Font styles to use
Sans Serif

Colors

Designer to choose colors to be used in the design.

Requirements
Must have
• Use current logo
• Need two card size options:
• Small Card: 70mm x 28mm (Landscape)
• Square Card: 65mm x 65mm
Nice to have
• I will need 8-10 files for each name, number and email address (details to follow)

```html
<!DOCTYPE html>
<html lang="en">
<head>
<meta charset="utf-8">
<title>Telmoro Limited – Business Cards</title>
<link rel="stylesheet" href="https://fonts.googleapis.com/css2?family=Montserrat:wght@400;500;700&family=Oswald:wght@600&display=swap">
<style>
  :root {
    --bg: #e9e9eb;
    --paper: #f6f6f4;
    --navy: #2b2a7a;
    --yellow: #f2d410;
    --green: #7cbf44;
    --blue: #2369b8;
    --orange: #e9a23b;
    --ink: #2a2a2e;
    --ink-soft: #55555c;
    --white: #ffffff;
  }
  * { box-sizing: border-box; margin: 0; padding: 0; }
  html, body { width: 1200px; height: 1093px; overflow: hidden; }
  body {
    position: relative;
    background: var(--bg);
    font-family: "Montserrat", Arial, sans-serif;
    color: var(--ink);
  }
  .card {
    position: absolute;
    width: 560px;
    height: 224px;
    background: var(--paper);
    overflow: hidden;
    box-shadow: 0 12px 28px rgba(0,0,0,0.18);
  }
  .wordmark {
    position: absolute;
    font-weight: 700;
    font-size: 34px;
    letter-spacing: 1px;
    display: flex;
    align-items: center;
    gap: 8px;
    white-space: nowrap;
  }
  .wordmark .mark-square { width: 14px; height: 14px; display: inline-block; }

  /* Card one: green side band */
  .card--band { left: 40px; top: 440px; }
  .card--band .side-band {
    position: absolute; left: 0; top: 0; bottom: 0; width: 78px;
    background: var(--green);
  }
  .card--band .side-label {
    position: absolute; left: 39px; top: 112px;
    transform: translate(-50%, -50%) rotate(-90deg);
    white-space: nowrap;
    font-size: 12px; font-weight: 500; letter-spacing: 4px; color: var(--ink);
  }
  .card--band .wordmark { right: 34px; top: 30px; color: var(--green); }
  .card--band .wordmark .mark-square { background: var(--green); }
  .card--band .holder { position: absolute; left: 104px; top: 118px; }
  .card--band .holder-name { font-size: 26px; font-weight: 500; color: var(--green); letter-spacing: -0.5px; }
  .card--band .holder-role { font-size: 10px; color: var(--ink); margin-top: -2px; }
  .card--band .address { position: absolute; left: 104px; top: 180px; font-size: 14px; color: var(--ink); letter-spacing: -0.3px; }
  .card--band .contact { position: absolute; right: 30px; top: 150px; font-size: 14px; line-height: 1.2; color: var(--ink); letter-spacing: -0.3px; white-space: nowrap; }

  /* Card two: navy and yellow split */
  .card--split { left: 600px; top: 150px; background: var(--navy); }
  .card--split .yellow-panel {
    position: absolute; right: 0; top: 0; bottom: 0; width: 205px;
    background: var(--yellow);
  }
  .card--split .wordmark { left: 28px; top: 24px; color: var(--white); }
  .card--split .wordmark .mark-square { background: var(--yellow); }
  .card--split .company {
    position: absolute; left: 28px; top: 82px;
    font-size: 16px; letter-spacing: 5px; color: var(--white); white-space: nowrap;
  }
  .card--split .address {
    position: absolute; left: 28px; top: 108px;
    font-size: 11px; letter-spacing: 3px; color: var(--white); white-space: nowrap;
  }
  .card--split .rule { position: absolute; left: 28px; top: 130px; width: 290px; height: 1px; background: var(--orange); }
  .card--split .holder { position: absolute; left: 28px; top: 158px; color: var(--white); }
  .card--split .holder::before { content: ""; display: block; width: 30px; height: 2px; background: var(--orange); margin-bottom: 6px; }
  .card--split .holder-name { font-size: 18px; letter-spacing: 2px; }
  .card--split .holder-role { font-size: 10px; letter-spacing: 1.5px; }
  .card--split .contact {
    position: absolute; right: 18px; top: 118px; width: 175px;
    font-size: 11px; letter-spacing: 1px; line-height: 1.7; color: var(--navy);
    text-align: right; white-space: nowrap;
  }
  .card--split .contact::before { content: ""; display: block; width: 30px; height: 2px; background: var(--navy); margin: 0 0 6px auto; }

  /* Card three: white with tricolour foot */
  .card--stripe { left: 600px; top: 720px; }
  .card--stripe .foot { position: absolute; left: 0; right: 0; bottom: 0; height: 14px; display: flex; }
  .card--stripe .foot span:nth-child(1) { flex: 35; background: var(--yellow); }
  .card--stripe .foot span:nth-child(2) { flex: 37; background: var(--blue); }
  .card--stripe .foot span:nth-child(3) { flex: 28; background: var(--navy); }
  .card--stripe .wordmark { left: 190px; top: 24px; color: var(--navy); }
  .card--stripe .wordmark .mark-square { background: var(--yellow); }
  .card--stripe .company { position: absolute; left: 190px; top: 76px; font-size: 15px; letter-spacing: 6px; color: var(--ink); white-space: nowrap; }
  .card--stripe .address { position: absolute; left: 190px; top: 100px; font-size: 10px; letter-spacing: 4px; color: var(--ink-soft); white-space: nowrap; }
  .card--stripe .holder { position: absolute; left: 26px; top: 150px; }
  .card--stripe .holder::before { content: ""; display: block; width: 30px; height: 2px; background: var(--orange); margin-bottom: 6px; }
  .card--stripe .holder-name { font-family: "Oswald", "Arial Narrow", sans-serif; font-weight: 600; font-size: 19px; letter-spacing: 2px; color: var(--ink); }
  .card--stripe .holder-role { font-size: 9px; letter-spacing: 1.5px; color: var(--ink); }
  .card--stripe .contact {
    position: absolute; right: 22px; top: 122px;
    font-size: 12px; letter-spacing: 2.5px; line-height: 1.5; color: var(--ink); white-space: nowrap;
  }
  .card--stripe .contact::before { content: ""; display: block; width: 30px; height: 2px; background: var(--orange); margin-bottom: 4px; }
</style>
</head>
<body>

  <article class="card card--split">
    <div class="yellow-panel"></div>
    <div class="wordmark"><span class="mark-square"></span>TELMORO</div>
    <div class="company">TELMORO LIMITED</div>
    <div class="address">STREET, AREA, POSTAL CODE</div>
    <div class="rule"></div>
    <div class="holder">
      <div class="holder-name">LENA MARSH</div>
      <div class="holder-role">EXECUTIVE MANAGER</div>
    </div>
    <div class="contact">+00-000 000 000<br>info@telmoromail.com</div>
  </article>

  <article class="card card--band">
    <div class="side-band"></div>
    <div class="side-label">TELMORO LIMITED</div>
    <div class="wordmark"><span class="mark-square"></span>TELMORO</div>
    <div class="holder">
      <div class="holder-name">Lena Marsh</div>
      <div class="holder-role">Executive Manager</div>
    </div>
    <div class="address">Street, Area, Postal code</div>
    <div class="contact">+00-000 000 000<br>info@telmoromail.com</div>
  </article>

  <article class="card card--stripe">
    <div class="wordmark"><span class="mark-square"></span>TELMORO</div>
    <div class="company">TELMORO LIMITED</div>
    <div class="address">STREET, AREA, POSTAL CODE</div>
    <div class="holder">
      <div class="holder-name">LENA MARSH</div>
      <div class="holder-role">EXECUTIVE MANAGER</div>
    </div>
    <div class="contact">+00-000 000 000<br>info@telmoromail.com</div>
    <div class="foot"><span></span><span></span><span></span></div>
  </article>

</body>
</html>
```